Business Card for New Convenience Store

We need a business card for our new convenience store using our logo. We want to have a color scheme and back ground created that will be transferable to other media platforms and advertising.

Industry/Entity Type

Convenience Store

```html
<!DOCTYPE html>
<html lang="en">
<head>
<meta charset="utf-8">
<title>Riverbend Mart – Business Card</title>
<link rel="stylesheet" href="https://fonts.googleapis.com/css2?family=Source+Sans+3:wght@400;700&display=swap">
<style>
  :root {
    --canvas: #ffffff;
    --card-bg: #221b18;
    --text-light: #ffffff;
    --accent-red: #c0000f;
    --sketch-dark: #2a2421;
    --sketch-light: #3b3431;
  }
  * { margin: 0; padding: 0; box-sizing: border-box; }
  html, body {
    width: 1200px;
    height: 1000px;
    overflow: hidden;
    background: var(--canvas);
    font-family: "Source Sans 3", sans-serif;
  }
  .stage { position: relative; width: 1200px; height: 1000px; }

  .card {
    position: absolute;
    left: 243px;
    width: 745px;
    height: 415px;
    background: var(--card-bg);
    color: var(--text-light);
    overflow: hidden;
  }
  .card--front { top: 66px; }
  .card--back { top: 525px; }

  /* Front */
  .brand-name {
    position: absolute;
    left: 50px;
    top: 46px;
    font-weight: 700;
    font-size: 46px;
    line-height: 1;
    letter-spacing: 0.5px;
  }
  .brand-name span { display: block; }
  .identity {
    position: absolute;
    right: 47px;
    top: 50px;
    text-align: right;
  }
  .identity__name {
    font-weight: 700;
    font-size: 35px;
    line-height: 1.05;
    letter-spacing: 0.5px;
  }
  .identity__title {
    font-weight: 400;
    font-size: 32px;
    line-height: 1.2;
  }
  .contact {
    position: absolute;
    right: 52px;
    top: 240px;
    text-align: right;
    list-style: none;
    font-size: 27px;
    line-height: 35px;
  }

  /* Back */
  .storefront-art {
    position: absolute;
    left: 0;
    top: 20px;
    width: 745px;
    height: 308px;
    background: linear-gradient(180deg, var(--sketch-dark) 0%, var(--sketch-light) 60%, var(--sketch-dark) 100%);
  }
  .address-band {
    position: absolute;
    left: 0;
    top: 328px;
    width: 745px;
    height: 49px;
    background: var(--accent-red);
    color: var(--text-light);
    font-size: 27px;
    line-height: 49px;
    text-align: center;
  }
</style>
</head>
<body>
<main class="stage">
  <section class="card card--front" aria-label="Business card front">
    <div class="brand-name"><span>RIVERBEND</span><span>MART</span></div>
    <div class="identity">
      <p class="identity__name">DANA WHITFIELD</p>
      <p class="identity__title">Manager</p>
    </div>
    <ul class="contact">
      <li>555-014-2290</li>
      <li>dwhitfield@rbmart.com</li>
      <li>42 Willow Bend Rd.</li>
      <li>Cedar Falls, AL 36999</li>
    </ul>
  </section>

  <section class="card card--back" aria-label="Business card back">
    <div class="storefront-art" role="img" aria-label="Grey line drawing of the store building exterior with the store name on its facade"></div>
    <p class="address-band">RBM: 42 Willow Bend Rd. | Cedar Falls, AL 36999</p>
  </section>
</main>
</body>
</html>
```